we need a new logo and business card and package label for my cake business.
looking for a fresh and standout design.

i have attached my old card to this.

Industry/Entity Type

Hospitality

Contact Information for Business Card

Rosalind Tremaine
email: rosit07@mailvex.net
facebook:www.faceplaza.net/rosiesweetovens
mobile:0438127906

Logo Text

Desserts By Rosie T

Font styles to use
Decorative

Colors
ed2930
f04a51
b768aa
0356a4
33a6d7

Requirements
Must have
• standout design
• grab attention

```html
<!DOCTYPE html>
<html lang="en">
<head>
<meta charset="utf-8">
<title>Desserts By Rosie T – Logo and Business Card</title>
<link rel="stylesheet" href="https://fonts.googleapis.com/css2?family=Arimo:wght@400;700&display=swap">
<style>
  :root {
    --backdrop: #c9c9c9;
    --paper: #ffffff;
    --sun-yellow: #f7c221;
    --band-yellow: #fcc010;
    --brand-red: #c0381c;
    --accent-orange: #e2552b;
    --cocoa: #6e2a1d;
    --ink-brown: #7a3b12;
  }
  * { box-sizing: border-box; margin: 0; padding: 0; }
  html, body { width: 1200px; height: 900px; overflow: hidden; }
  body {
    background: var(--backdrop);
    font-family: "Arimo", Arial, sans-serif;
    position: relative;
  }

  /* Logo presentation disc */
  .logo-showcase {
    position: absolute;
    left: 40px; top: 470px;
    width: 400px; height: 400px;
    border-radius: 50%;
    background: var(--paper);
    display: flex; align-items: center; justify-content: center;
  }
  .logo-lockup {
    display: flex; flex-direction: column; align-items: center; gap: 18px;
  }
  .logo-dot {
    width: 90px; height: 90px; border-radius: 50%;
    background: var(--sun-yellow);
  }
  .logo-name {
    font-weight: 700; font-size: 30px; color: var(--cocoa);
  }

  /* Business cards */
  .card {
    position: absolute;
    width: 560px; height: 320px;
    background: var(--paper);
    overflow: hidden;
    box-shadow: 0 6px 18px rgba(0,0,0,0.18);
  }
  .card--front { left: 560px; top: 60px; }
  .card--back  { left: 560px; top: 430px; }

  .front-emblem {
    position: absolute;
    left: 180px; top: 50px;
    width: 360px; height: 360px;
    border-radius: 50%;
    background: var(--sun-yellow);
  }
  .front-name {
    position: absolute;
    left: 230px; top: 140px;
    width: 260px;
    text-align: center;
    font-weight: 700; font-size: 30px; color: var(--cocoa);
  }

  .back-body {
    position: absolute; left: 0; right: 0; top: 24px;
    display: flex; flex-direction: column; align-items: center;
    text-align: center;
  }
  .back-dot {
    width: 54px; height: 54px; border-radius: 50%;
    background: var(--sun-yellow);
    margin-bottom: 12px;
  }
  .business-name {
    font-weight: 700; font-size: 30px; color: var(--brand-red);
    margin-bottom: 12px;
  }
  .person-name {
    font-weight: 700; font-size: 19px; color: var(--accent-orange);
    margin-bottom: 4px;
  }
  .person-role {
    font-size: 14px; color: var(--accent-orange);
  }
  .contact-band {
    position: absolute; left: 0; right: 0; bottom: 0;
    height: 80px;
    background: var(--band-yellow);
    display: flex; flex-direction: column; align-items: center; justify-content: center;
    gap: 6px;
    font-size: 14px; color: var(--ink-brown);
  }
</style>
</head>
<body>

  <div class="logo-showcase">
    <div class="logo-lockup">
      <div class="logo-dot"></div>
      <div class="logo-name">Desserts By Rosie T</div>
    </div>
  </div>

  <section class="card card--front" aria-label="Business card front">
    <div class="front-emblem"></div>
    <div class="front-name">Desserts By Rosie T</div>
  </section>

  <section class="card card--back" aria-label="Business card back">
    <div class="back-body">
      <div class="back-dot"></div>
      <h1 class="business-name">Desserts By Rosie T</h1>
      <p class="person-name">Rosalind Tremaine</p>
      <p class="person-role">Qualified Chef and Pasty Chef</p>
    </div>
    <div class="contact-band">
      <p class="contact-line">Mobile: 0438127906</p>
      <p class="contact-line">Email: rosit07@mailvex.net | www.faceplaza.net/rosiesweetovens</p>
    </div>
  </section>

</body>
</html>
```